Maple Yard Works Website Design

I need a 6 page website design for a company that Installs Synthetic Turf, Interlocking Pavers, and Patio Covers. We would like to see the design us "Landscaping Style" of a look and feel. Green, Blacks and Gray colors. Initially the website will be used the online brochure but landing pages will need to be built form this original design. Since this is brand new start up (actually offshoot form another company I was part of) we are limited on photography. We will need to use stock images until i can get installed projects photographed.This is a B2C site...targeting homeowners who are looking to expand their back yards or simply transition to maintenance free and drought tolerant yards. This is becoming very popular in California and along the Southwest United States.

Target Market(s)

Homeowners

Industry/Entity Type

Home Improvement

Coding

Coded - Design and coding required

Number of Pages Required

1 page

Font styles to use
Sans Serif

Colors
9bcb3b

Requirements
Must have
• Strong visuals and some graphic elements to illustrate the services.
• Here are some sample sites:
• https://brelvanstone.com
• https://www.quintaleaf.net/
• https://plomaris.com/BackyardHomePage
• https://otterlawns.com
• https://www.greskano.com/
• http://www.brookvalestones.com/
• https://meadowblendsupplyco.com/
• https://decktraderdepotco.com
• https://www.welbrickbuilders.com

```html
<!DOCTYPE html>
<html lang="en">
<head>
<meta charset="utf-8">
<title>Maple Yard Works</title>
<link href="https://fonts.googleapis.com/css2?family=Ubuntu:wght@400;500;700&family=Open+Sans:wght@400;600&display=swap" rel="stylesheet">
<style>
:root{
  --green:#5fae2a;
  --green-light:#9bcb3b;
  --green-dark:#3f8a1a;
  --black:#1b1b1b;
  --ink:#2a2a2a;
  --gray:#7a7a7a;
  --gray-bg:#f2f2f2;
  --line:#dcdcdc;
  --white:#ffffff;
  --footer:#202020;
}
*{box-sizing:border-box;margin:0;padding:0}
html,body{width:1200px;height:4288px;overflow:hidden}
body{position:relative;background:var(--white);font-family:'Open Sans',Arial,sans-serif;color:var(--ink)}
.abs{position:absolute}
.heading{font-family:'Ubuntu',Arial,sans-serif;font-weight:500;color:var(--ink);letter-spacing:1px}
.body-text{font-size:14px;line-height:24px;color:var(--gray)}
.btn{position:absolute;display:flex;align-items:center;justify-content:center;background:var(--green);color:#fff;font-family:'Ubuntu',Arial,sans-serif;font-size:15px;font-weight:500;letter-spacing:.5px}
.photo{position:absolute}

/* header */
.site-header{position:absolute;left:0;top:0;width:1200px;height:116px;background:#fff}
.brand{left:76px;top:26px;font-family:'Ubuntu',Arial,sans-serif}
.brand-name{font-size:36px;font-weight:700;color:var(--black);letter-spacing:1px;line-height:40px}
.brand-sub{font-size:17px;font-weight:700;color:var(--black);letter-spacing:1px}
.call-box{right:76px;top:24px;display:flex;align-items:center;gap:16px}
.call-icon{width:56px;height:56px;border:2px solid var(--line);display:flex;align-items:center;justify-content:center}
.call-label{font-size:14px;color:var(--gray)}
.call-number{font-family:'Ubuntu',sans-serif;font-size:24px;font-weight:500;color:var(--black)}
.main-nav{position:absolute;left:0;top:116px;width:1200px;height:44px;background:var(--green)}
.nav-links{left:76px;top:0;height:44px;display:flex;align-items:center;gap:0}
.nav-links a{color:#fff;text-decoration:none;font-size:14px;font-family:'Ubuntu',sans-serif;padding:0 14px;line-height:44px}
.nav-links a.active{background:var(--green-dark)}
.nav-cta{right:76px;top:0;width:168px;height:44px;background:var(--black);color:#fff;display:flex;align-items:center;justify-content:center;font-family:'Ubuntu',sans-serif;font-size:16px;font-weight:500}

/* hero */
.hero{left:0;top:160px;width:1200px;height:552px;background:linear-gradient(180deg,#2c3a25 0%,#3f5430 45%,#2a3322 100%)}
.hero-title{left:0;top:380px;width:1200px;text-align:center;font-family:'Ubuntu',sans-serif;font-size:30px;font-weight:500;color:#fff;letter-spacing:2px}
.hero-text{left:250px;top:428px;width:700px;text-align:center;color:#e8e8e8;font-size:16px;line-height:26px}

/* services */
.section-title{left:0;width:1200px;text-align:center;font-size:34px}
.service-card{position:absolute;top:832px;width:324px;height:280px;background:#fff;box-shadow:0 2px 8px rgba(0,0,0,.12)}
.service-photo{left:0;top:0;width:324px;height:216px}
.service-label{position:absolute;left:16px;top:232px;font-size:15px;color:var(--ink)}
.service-badge{position:absolute;right:0;top:216px;width:64px;height:64px;background:var(--green);display:flex;align-items:center;justify-content:center}

/* welcome */
.welcome-title{left:76px;top:1222px;font-size:34px;line-height:44px}
.welcome-text{left:76px;top:1332px;width:540px}
.welcome-photo{left:686px;top:1222px;width:420px;height:280px}
.welcome-frame{left:736px;top:1262px;width:420px;height:280px;border:3px solid #ececec}

/* touch & testimonial */
.band{left:0;top:1644px;width:1200px;height:620px;background:var(--gray-bg)}
.touch-photo{left:0;top:1644px;width:334px;height:620px}
.form-card{left:168px;top:1724px;width:412px;height:460px;background:#fff;box-shadow:0 3px 12px rgba(0,0,0,.12)}
.form-title{position:absolute;left:0;top:52px;width:100%;text-align:center;font-size:30px}
.field{position:absolute;left:48px;width:316px;height:42px;border:1px solid var(--line);font-size:13px;color:#999;padding:12px 14px}
.clients-title{left:660px;top:1752px;font-size:34px}
.client-avatar{left:660px;top:1830px;width:80px;height:80px}
.client-name{left:768px;top:1842px;font-family:'Ubuntu',sans-serif;font-size:20px;color:var(--green)}
.client-role{left:768px;top:1876px;font-size:14px;color:var(--gray)}
.client-rule{left:660px;top:1980px;width:464px;height:1px;background:var(--line)}
.client-quote{left:660px;top:2010px;width:464px}
.dots{left:660px;top:2146px;display:flex;gap:8px}
.dots span{display:block;width:28px;height:4px;background:#bbb}
.dots span.on{background:var(--ink)}

/* gallery */
.tile{position:absolute}

/* news */
.news-band{left:0;top:3262px;width:1200px;height:300px;background:linear-gradient(135deg,var(--green-light),var(--green))}
.news-title{left:76px;top:3350px;font-size:34px;color:#fff}
.news-intro{left:76px;top:3410px;width:240px;color:#fff;font-size:14px;line-height:22px}
.news-arrows{left:76px;top:3480px;display:flex;gap:16px}
.news-arrows span{display:flex;align-items:center;justify-content:center;width:96px;height:38px;border:1px solid rgba(255,255,255,.7);color:#fff;font-size:13px;font-family:'Ubuntu',sans-serif}
.news-card{left:390px;top:3312px;width:734px;height:350px;background:#fff;box-shadow:0 3px 14px rgba(0,0,0,.15)}
.news-photo{left:436px;top:3352px;width:320px;height:230px}
.news-head{left:800px;top:3400px;font-family:'Ubuntu',sans-serif;font-size:24px;font-weight:500;color:var(--ink)}
.news-rule{left:800px;top:3456px;width:280px;height:1px;background:var(--line)}
.news-body{left:800px;top:3486px;width:300px}

/* quick contact */
.quick-title{left:76px;top:3800px;font-size:26px;line-height:34px}
.quick-title em{font-style:normal;color:var(--green)}
.quick-text{left:76px;top:3882px;font-size:14px;color:var(--gray)}
.quick-call{left:648px;top:3846px;font-family:'Ubuntu',sans-serif;font-size:20px;font-weight:500;color:var(--ink)}
.quick-call em{font-style:normal;color:var(--green)}

/* footer */
.footer{left:0;top:3964px;width:1200px;height:270px;background:var(--footer)}
.footer-brand{left:76px;top:4020px;font-family:'Ubuntu',sans-serif;color:#fff}
.footer-brand .brand-name{color:#fff}
.footer-brand .brand-sub{color:#fff}
.footer-about{left:76px;top:4112px;width:290px;color:#bdbdbd;font-size:14px;line-height:22px}
.footer-head{font-family:'Ubuntu',sans-serif;font-size:18px;font-weight:500;color:#fff}
.footer-rule{width:40px;height:2px;background:var(--green);margin-top:8px}
.footer-links{display:grid;grid-template-columns:190px 150px;row-gap:14px;margin-top:22px}
.footer-links span{color:#cfcfcf;font-size:14px;display:flex;align-items:center;gap:12px}
.footer-links span::before{content:"";width:6px;height:6px;border-radius:50%;background:var(--green)}
.footer-contact{margin-top:22px;display:flex;flex-direction:column;gap:14px}
.footer-contact div{display:flex;gap:12px;color:#cfcfcf;font-size:14px;line-height:20px}
.footer-bar{left:0;top:4234px;width:1200px;height:54px;background:var(--green);color:#fff;font-size:12px;display:flex;align-items:center;justify-content:center;letter-spacing:.5px}
</style>
</head>
<body>

<header class="site-header">
  <div class="abs brand">
    <div class="brand-name">MAPLE YARD</div>
    <div class="brand-sub">WORKS</div>
  </div>
  <div class="abs call-box">
    <div class="call-icon">
      <svg width="24" height="24" viewBox="0 0 24 24"><path d="M6.6 10.8a15.1 15.1 0 0 0 6.6 6.6l2.2-2.2a1 1 0 0 1 1-.25 11.4 11.4 0 0 0 3.6.57 1 1 0 0 1 1 1V20a1 1 0 0 1-1 1A17 17 0 0 1 3 4a1 1 0 0 1 1-1h3.5a1 1 0 0 1 1 1c0 1.25.2 2.45.57 3.57a1 1 0 0 1-.25 1z" fill="#1b1b1b"/></svg>
    </div>
    <div>
      <div class="call-label">CALL US ON</div>
      <div class="call-number">123 456 7800</div>
    </div>
  </div>
</header>

<nav class="main-nav">
  <div class="abs nav-links">
    <a class="active">HOME</a><a>ABOUT</a><a>SERVICES</a><a>GALLERY</a><a>NEWS</a><a>CONTACT</a>
  </div>
  <div class="abs nav-cta">GET IN TOUCH</div>
</nav>

<section>
  <div class="abs hero" role="img" aria-label="Dark-toned photo of a landscaped backyard garden with lawn and shrubs"></div>
  <h1 class="abs hero-title">MAPLE YARD WORKS</h1>
  <p class="abs hero-text">Lorem Ipsum is simply dummy text of the printing and typesetting industry. Lorem Ipsum has been the industry's standard dummy text ever.</p>
</section>

<section>
  <h2 class="abs heading section-title" style="top:764px">OUR SERVICES</h2>
  <div class="service-card" style="left:76px">
    <div class="photo service-photo" role="img" aria-label="Photo of synthetic turf lawn with curved garden edging" style="background:linear-gradient(160deg,#5e8f3a,#7fb04a 60%,#c9c4b5)"></div>
    <div class="service-label">Installs Synthetic Turf</div>
    <div class="service-badge"><svg width="34" height="34" viewBox="0 0 34 34"><path d="M4 28c4-10 6-14 7-20M12 28c1-8 3-12 6-16M20 28c2-7 5-11 10-14M2 30h30" stroke="#fff" stroke-width="2.4" fill="none" stroke-linecap="round"/></svg></div>
  </div>
  <div class="service-card" style="left:440px">
    <div class="photo service-photo" role="img" aria-label="Photo of interlocking paver walkway with shrubs" style="background:linear-gradient(160deg,#9a9a92,#c2c0b8 55%,#6f8f4a)"></div>
    <div class="service-label">Interlocking Pavers</div>
    <div class="service-badge"><svg width="34" height="34" viewBox="0 0 34 34"><circle cx="17" cy="17" r="14" fill="none" stroke="#fff" stroke-width="2.4"/><path d="M7 12h20M7 22h20M13 12v10M21 4v8M21 22v8" stroke="#fff" stroke-width="2.4"/></svg></div>
  </div>
  <div class="service-card" style="left:800px">
    <div class="photo service-photo" role="img" aria-label="Photo of a wooden patio cover pergola over a lawn" style="background:linear-gradient(170deg,#d9d4c6,#b49a78 50%,#6f9448)"></div>
    <div class="service-label">Patio Covers</div>
    <div class="service-badge"><svg width="34" height="34" viewBox="0 0 34 34"><path d="M3 12 17 5l14 7M7 12v16M27 12v16M4 16h26" stroke="#fff" stroke-width="2.4" fill="none" stroke-linejoin="round"/></svg></div>
  </div>
</section>

<section>
  <h2 class="abs heading welcome-title">WELCOME TO<br>MAPLE YARD WORKS</h2>
  <div class="abs body-text welcome-text">
    <p>Lorem Ipsum is simply dummy text of the printing and typesetting industry. Lorem Ipsum has been the industry's standard dummy text ever since the 1500s, when an unknown printer took a galley.</p>
    <p style="margin-top:14px">It has survived not only five centuries, but also the leap into electronic typesetting, remaining essentially unchanged. It was popularised in th...</p>
  </div>
  <div class="btn" style="left:76px;top:1488px;width:188px;height:52px">GET IN TOUCH</div>
  <div class="abs welcome-frame"></div>
  <div class="photo welcome-photo" role="img" aria-label="Photo of a lawn beside a curved paver path and stone steps" style="background:linear-gradient(150deg,#2f5a22,#5f9a36 55%,#b8b3a6)"></div>
</section>

<section>
  <div class="abs band"></div>
  <div class="photo touch-photo" role="img" aria-label="Photo of a patio with lounge chairs beside a house and lawn" style="background:linear-gradient(180deg,#8a8e90,#6b5a48 55%,#4f7e2e)"></div>
  <div class="abs form-card">
    <h3 class="heading form-title">GET IN TOUCH</h3>
    <div class="field" style="top:122px">Name</div>
    <div class="field" style="top:178px">Email</div>
    <div class="field" style="top:234px">Phone</div>
    <div class="field" style="top:290px">Subject</div>
    <div class="btn" style="left:118px;top:366px;width:176px;height:46px">SUBMIT</div>
  </div>
  <h2 class="abs heading clients-title">WHAT OUR CLIENTS SAY</h2>
  <div class="photo client-avatar" role="img" aria-label="Customer portrait photo" style="background:linear-gradient(160deg,#c9b39a,#8a7460)"></div>
  <div class="abs client-name">Name Surname</div>
  <div class="abs client-role">Customer</div>
  <div class="abs client-rule"></div>
  <p class="abs body-text client-quote">Lorem Ipsum is simply dummy text of the printing and typesetting industry. Lorem Ipsum has been the industry's standard dummy text ever since the 1500s, when an unknown printer took a galley. It has survived not only five centuries, but also the leap into electronic type.</p>
  <div class="abs dots"><span class="on"></span><span></span><span></span></div>
</section>

<section>
  <h2 class="abs heading section-title" style="top:2322px">PROJECT GALLERY</h2>
  <div class="tile" style="left:76px;top:2404px;width:260px;height:340px;background:linear-gradient(170deg,#8a5a3e,#6f9a44 45%,#5c8c33)" role="img" aria-label="Photo of artificial turf beside a brick wall planter"></div>
  <div class="tile" style="left:336px;top:2404px;width:264px;height:340px;background:linear-gradient(150deg,#7e7e78,#bdbab0 50%,#5c5a55)" role="img" aria-label="Photo of grey paver steps"></div>
  <div class="tile" style="left:600px;top:2404px;width:524px;height:340px;background:linear-gradient(170deg,#6f7a5c,#9a7a5c 50%,#b09078)" role="img" aria-label="Photo of a paved patio with a round fire pit and seating"></div>
  <div class="tile" style="left:76px;top:2744px;width:524px;height:348px;background:linear-gradient(170deg,#4f7a2e,#8a4a2e 50%,#a0603a)" role="img" aria-label="Photo of a wooden deck with furniture under trees"></div>
  <div class="tile" style="left:600px;top:2744px;width:256px;height:348px;background:linear-gradient(160deg,#6c6a62,#9a968a 50%,#5f8a3a)" role="img" aria-label="Photo of a curved stone retaining wall with lawn"></div>
  <div class="tile" style="left:856px;top:2744px;width:268px;height:348px;background:linear-gradient(170deg,#5a8a3a,#a89888 55%,#8a7a6a)" role="img" aria-label="Photo of a deck with patio umbrella and greenery"></div>
  <div class="btn" style="left:504px;top:3136px;width:192px;height:52px">VIEW MORE</div>
</section>

<section>
  <div class="abs news-band"></div>
  <h2 class="abs heading news-title">LATEST NEWS</h2>
  <p class="abs news-intro">Lorem Ipsum is simply dummy text of the printing and typesetting industry.</p>
  <div class="abs news-arrows"><span>&larr;&nbsp;&nbsp;NEXT</span><span>PREV&nbsp;&nbsp;&rarr;</span></div>
  <div class="abs news-card"></div>
  <div class="photo news-photo" role="img" aria-label="Photo of stepping stones set in a green lawn" style="background:linear-gradient(150deg,#3f7a22,#7fb63e 55%,#5a9a2e)"></div>
  <div class="abs news-head">Lorem Ipsum is simply dumy.</div>
  <div class="abs news-rule"></div>
  <p class="abs body-text news-body">Lorem Ipsum is simply dummy text of the printing and typesetting industry. Lorem Ipsum has been the industry's standard dummy text.</p>
</section>

<section>
  <h2 class="abs heading quick-title">GET QUICK CONTACT TO<br><em>MAPLE YARD WORKS</em></h2>
  <p class="abs quick-text">Lorem Ipsum is simply dummy text of the printing and typesetting.</p>
  <div class="abs quick-call">CALL US ON <em>123 456 7800</em></div>
  <div class="btn" style="left:936px;top:3830px;width:188px;height:56px">CONTACT US</div>
</section>

<footer>
  <div class="abs footer"></div>
  <div class="abs footer-brand">
    <div class="brand-name">MAPLE YARD</div>
    <div class="brand-sub">WORKS</div>
  </div>
  <p class="abs footer-about">Lorem Ipsum is simply dummy text of the printing and typesetting industry.</p>
  <div class="abs" style="left:440px;top:4020px">
    <div class="footer-head">SITEMAP</div>
    <div class="footer-rule"></div>
    <div class="footer-links">
      <span>Home</span><span>News</span>
      <span>About us</span><span>Gallery</span>
      <span>Services</span><span>Contact</span>
    </div>
  </div>
  <div class="abs" style="left:800px;top:4020px">
    <div class="footer-head">GET IN TOUCH</div>
    <div class="footer-rule"></div>
    <div class="footer-contact">
      <div><svg width="16" height="20" viewBox="0 0 16 20"><path d="M8 0a7 7 0 0 0-7 7c0 5 7 13 7 13s7-8 7-13a7 7 0 0 0-7-7zm0 10a3 3 0 1 1 0-6 3 3 0 0 1 0 6z" fill="#5fae2a"/></svg><span>Lorem Ipsum is simply dummy text<br>of the printing and typesetting.</span></div>
      <div><svg width="16" height="16" viewBox="0 0 24 24"><path d="M6.6 10.8a15.1 15.1 0 0 0 6.6 6.6l2.2-2.2a1 1 0 0 1 1-.25 11.4 11.4 0 0 0 3.6.57 1 1 0 0 1 1 1V20a1 1 0 0 1-1 1A17 17 0 0 1 3 4a1 1 0 0 1 1-1h3.5a1 1 0 0 1 1 1c0 1.25.2 2.45.57 3.57a1 1 0 0 1-.25 1z" fill="#5fae2a"/></svg><span>123 456 7800</span></div>
    </div>
  </div>
  <div class="abs footer-bar">MAPLE YARD WORKS 2019 - All Rights Reserved</div>
</footer>

</body>
</html>
```